LSCo Wholesale Flyer

I need a wholesaler flyer/letter put together. I've provided copy and a range of photos for the designer to use. The flyer needs to match the same colour pallet and style of larkfieldseedhouseco.com.au.

It will be used to send to new potenial retailers so needs to look smick.

```html
<!DOCTYPE html>
<html lang="en">
<head>
<meta charset="utf-8">
<title>LSCo Wholesale Flyer</title>
<link href="https://fonts.googleapis.com/css2?family=Federo&family=Open+Sans:wght@400;600;700&display=swap" rel="stylesheet">
<style>
:root{
  --forest:#3b4038;
  --forest-deep:#2e322c;
  --cream:#f1e8d8;
  --cream-soft:#f6efe3;
  --sand:#e4d6bd;
  --ink:#2b2b27;
  --muted:#5a5a52;
  --gold:#d9b23c;
  --sale:#c8242f;
  --photo-dark:#4a3a2c;
  --photo-warm:#9a7b58;
  --page:#f2ece2;
}
*{margin:0;padding:0;box-sizing:border-box}
html,body{width:927px;height:1200px;overflow:hidden}
body{background:var(--page);font-family:"Open Sans",Arial,sans-serif;color:var(--ink);position:relative}
.display{font-family:"Federo","Times New Roman",serif;font-weight:400}
.spread{position:absolute;left:146px;width:665px;height:514px;display:flex;box-shadow:0 6px 18px rgba(60,50,35,.18)}
.spread--outside{top:61px}
.spread--inside{top:625px}
.panel{position:relative;overflow:hidden;height:100%}
.panel--a{width:220px}
.panel--b{width:230px}
.panel--c{width:215px}
.abs{position:absolute}
.photo{position:absolute}
.bg-svg{position:absolute;left:0;top:0}

/* cover */
.cover{background:linear-gradient(180deg,var(--cream-soft),var(--sand))}
.cover__photo{left:0;top:0;width:220px;height:270px;background:linear-gradient(160deg,#2a211a,var(--photo-dark) 45%,#7a6048)}
.brand-mark{font-family:"Open Sans",Arial,sans-serif;font-weight:600;color:#f5efe4}
.cover__logo{left:18px;top:28px;font-size:13px}
.cover__title{left:18px;top:76px;font-size:25px;line-height:1.05;color:#f5efe4;letter-spacing:.5px}
.cover__seal{left:84px;top:228px;width:60px;height:60px;border-radius:50%;background:#fff;display:flex;align-items:center;justify-content:center}
.cover__seal span{width:40px;height:40px;border-radius:50%;background:#4a4a46;color:#fff;display:flex;align-items:center;justify-content:center;font-size:8px;font-weight:600}
.cover__headline{left:0;width:220px;top:302px;text-align:center;font-size:23px;line-height:1.06;color:#55574d}
.cover__tag{left:0;width:220px;top:389px;text-align:center;font-size:7px;font-weight:700;letter-spacing:.2px}
.cover__body{left:28px;width:166px;top:404px;text-align:center;font-size:5.6px;line-height:1.3;color:var(--muted)}
.cover__foot{left:0;top:435px;width:220px;height:79px;background:linear-gradient(120deg,#efe6d6,#d8c8ad 60%,#b9a88a)}

/* story / price list */
.story{background:linear-gradient(180deg,#f4ecdc,#ebe0c9 60%,#d9cdb4)}
.story__title{left:0;width:229px;top:46px;text-align:center;font-size:21px;color:#3f4139}
.story__intro{left:22px;width:186px;top:77px;text-align:center;font-size:6.1px;line-height:1.35}
.range-head{left:0;width:229px;text-align:center;font-size:7px;font-weight:700;letter-spacing:.2px}
.item-name{left:12px;font-size:5.6px;font-weight:700}
.price-bar{left:10px;width:208px;height:11px;background:var(--forest);color:#eee8dc;font-size:3.9px;display:flex;align-items:center;justify-content:space-between;padding:0 5px}
.price-bar b{font-weight:600;margin-right:4px}

/* order sheet */
.order{background:var(--cream-soft)}
.order__photo{left:0;top:0;width:215px;height:250px;background:linear-gradient(180deg,#e8e4dd,#cfc6b9 60%,#b7a590)}
.order__title{left:20px;top:198px;font-size:24px;line-height:1.02;color:#f0e9dc}
.order__copy{left:20px;width:185px;top:255px;font-size:6.2px;line-height:1.33;color:#dcd7cc}
.order__copy p{margin-bottom:3.5px}
.form{left:20px;width:177px;top:362px}
.form__row{display:flex;align-items:flex-end;height:15.2px;font-size:8px;color:#e8e3d8}
.form__row span{white-space:nowrap;margin-right:6px}
.form__row i{flex:1;border-bottom:.6px solid #bdb8ad;margin-bottom:2px}
.badge{left:154px;top:140px;width:50px;height:50px;border-radius:50%;background:var(--sale);color:#fff;display:flex;flex-direction:column;align-items:center;justify-content:center;font-weight:700;line-height:.95;font-size:11px}
.badge span:last-child{color:#f4c843}
.order__web{left:0;width:215px;top:497px;text-align:center;font-size:7.4px;font-weight:700}
.globe{display:inline-block;width:6px;height:6px;border:.8px solid var(--ink);border-radius:50%;vertical-align:-0.5px;margin-right:3px}

/* inside: ingredients */
.inside-a{background:linear-gradient(180deg,#f3ebdd,#e6d9c1)}
.strip-photo{left:0;top:0;height:90px;background:linear-gradient(180deg,#8a9478,#6c735d 55%,#4c4a3d)}
.feature-img{width:73px;height:61px;border-radius:30px 8px 30px 8px;background:linear-gradient(135deg,var(--photo-warm),var(--photo-dark))}
.feature-img--r{border-radius:8px 30px 8px 30px}
.feature-title{font-size:8.2px;font-weight:700}
.feature-rule{height:.6px;background:#9b958a;width:100px;margin:3px 0 4px}
.feature-text{font-size:5.8px;line-height:1.25;color:var(--muted)}
.feature--r .feature-title,.feature--r .feature-text{text-align:right}

/* inside: oils */
.inside-b{background:var(--forest)}
.oil-title{font-size:6.8px;color:#efe9dc}
.oil-text{font-size:5.6px;line-height:1.28;color:#c9c6bb}
.thumb{position:absolute;border-radius:4px;background:linear-gradient(135deg,#d9cfbd,#8a7358)}
.ticks{display:grid;grid-template-columns:1fr 1fr;gap:2px 6px;list-style:none;font-size:5px;color:#dcd9cf}
.ticks li{display:flex;align-items:center;gap:2px}
.tick{width:5px;height:5px;border:.6px solid currentColor;border-radius:50%;font-size:3.6px;line-height:4px;text-align:center}
.contact{left:0;top:476px;width:230px;height:38px;background:var(--cream-soft)}
.contact__head{left:14px;top:20px;font-size:6.5px;font-weight:700}
.contact__line{left:14px;top:31px;font-size:4.6px;font-weight:600;display:flex;gap:8px;white-space:nowrap}

/* inside: scents */
.inside-c{background:linear-gradient(180deg,#f3ebdd,#e5d8bf)}
.scent-head{left:0;top:0;width:215px;height:96px;background:var(--forest)}
.scent-logo{left:14px;top:14px;font-size:8px}
.scent-tagline{left:120px;width:88px;top:13px;font-size:3.9px;color:#dcd7cc;text-align:right;line-height:1.3}
.scent-heading{left:14px;top:38px;font-size:13px;line-height:1.08;color:#ebe4d6}
.arch{background:linear-gradient(180deg,#e9dfd2,#c9b8a2);border-radius:30px 30px 6px 30px}
.col-title{font-size:6.6px;font-weight:700}
.col-rule{height:.6px;background:#8d877c;margin:2px 0 3px}
.col-text{font-size:4.2px;line-height:1.32;color:var(--muted)}
.why{font-size:21px;line-height:1;color:#2f312c}
.why small{display:block;font-size:9px;margin-top:1px}
.mini-ticks{display:grid;grid-template-columns:1fr 1fr;gap:4px 4px;list-style:none;font-size:4.1px}
.mini-ticks li{display:flex;align-items:center;gap:2px}
</style>
</head>
<body>

<!-- ============ OUTSIDE SPREAD ============ -->
<section class="spread spread--outside">

  <!-- Cover -->
  <article class="panel panel--a cover">
    <div class="photo cover__photo" role="img" aria-label="Photo of a lit amber candle jar on a dark dining table"></div>
    <svg class="bg-svg" width="220" height="300" viewBox="0 0 220 300" aria-hidden="true">
      <path d="M0 270 C60 250 130 232 220 190 L220 300 L0 300 Z" fill="#f1e8d8"/>
      <path d="M90 262 C140 240 180 222 220 200 L220 212 C180 232 140 250 96 268 Z" fill="#3b4038"/>
    </svg>
    <div class="abs brand-mark cover__logo">LSCo.</div>
    <h1 class="abs display cover__title">LARKFIELD<br>SEEDHOUSE<br>CO.</h1>
    <div class="abs cover__seal"><span>LSCo.</span></div>
    <h2 class="abs display cover__headline">Handcrafted<br>Botanical<br>Products</h2>
    <p class="abs cover__tag">PURE INGREDIENTS. HONEST PRODUCTS.</p>
    <p class="abs cover__body">We create small-batch botanical skincare using Australian-grown ingredients.Our mission is to bring natural luxury into everyday routines.</p>
    <div class="photo cover__foot" role="img" aria-label="Photo of soap bars, cream tins and dried lavender sprigs"></div>
    <svg class="bg-svg" style="top:420px" width="220" height="94" viewBox="0 0 220 94" aria-hidden="true">
      <path d="M150 94 C170 70 200 55 220 20 L220 94 Z" fill="#3b4038"/>
      <path d="M135 94 C155 72 190 60 220 34 L220 42 C195 64 165 78 146 94 Z" fill="#f1e8d8"/>
    </svg>
  </article>

  <!-- Price list -->
  <article class="panel panel--b story">
    <svg class="bg-svg" width="229" height="70" viewBox="0 0 229 70" aria-hidden="true">
      <path d="M0 0 H85 C75 30 40 40 0 55 Z" fill="#4a3a2c"/>
      <path d="M0 55 C40 40 75 30 85 0 H92 C82 34 46 46 0 62 Z" fill="#f6efe3"/>
    </svg>
    <h2 class="abs display story__title">OUR STORY</h2>
    <p class="abs story__intro">Larkfield Seedhouse Co. is a small, family-owned business based on our property, Kestrel Hill Farm, in historic Ellerby, Tasmania. Since 2014.</p>

    <h3 class="abs range-head" style="top:113px">CANDLE RANGE</h3>

    <p class="abs item-name" style="top:128px">Wild Highland Fern</p>
    <div class="abs price-bar" style="top:145px"><span><b>LARGE</b>$35.00 - $62.00</span><span><b>MEDIUM</b>$23.00 - $42.00</span><span><b>SMALL</b>$17.00 - $30.00</span></div>
    <p class="abs item-name" style="top:160px">Mountain Pepper and Dark Berry</p>
    <div class="abs price-bar" style="top:178px"><span><b>LARGE</b>$35.00 - $62.00</span><span><b>MEDIUM</b>$23.00 - $42.00</span><span><b>SMALL</b>$17.00 - $30.00</span></div>
    <p class="abs item-name" style="top:194px">Southern Shoreline</p>
    <div class="abs price-bar" style="top:212px"><span><b>LARGE</b>$35.00 - $62.00</span><span><b>MEDIUM</b>$23.00 - $42.00</span><span><b>SMALL</b>$17.00 - $30.00</span></div>
    <p class="abs item-name" style="top:229px">Lavender Meadow</p>
    <div class="abs price-bar" style="top:247px"><span><b>LARGE</b>$35.00 - $62.00</span><span><b>MEDIUM</b>$23.00 - $42.00</span><span><b>SMALL</b>$17.00 - $30.00</span></div>
    <p class="abs item-name" style="top:264px">Alpine Dew</p>
    <div class="abs price-bar" style="top:283px"><span><b>LARGE</b>$35.00 - $62.00</span><span><b>MEDIUM</b>$23.00 - $42.00</span><span><b>SMALL</b>$17.00 - $30.00</span></div>
    <p class="abs item-name" style="top:299px">Hearth Ember</p>
    <div class="abs price-bar" style="top:318px"><span><b>LARGE</b>$35.00 - $62.00</span><span><b>MEDIUM</b>$23.00 - $42.00</span><span><b>SMALL</b>$17.00 - $30.00</span></div>
    <p class="abs item-name" style="top:333px">Old Cedar Grove</p>
    <div class="abs price-bar" style="top:352px"><span><b>LARGE</b>$35.00 - $62.00</span><span><b>MEDIUM</b>$23.00 - $42.00</span><span><b>SMALL</b>$17.00 - $30.00</span></div>
    <p class="abs item-name" style="top:368px">Christmas (seasonal)</p>
    <div class="abs price-bar" style="top:386px"><span><b>LARGE</b>$35.00 - $62.00</span><span><b>MEDIUM</b>$23.00 - $42.00</span><span><b>SMALL</b>$17.00 - $30.00</span></div>

    <h3 class="abs range-head" style="top:407px">SOAP AND BODY WASH</h3>

    <p class="abs item-name" style="top:422px">Old Cedar Grove</p>
    <div class="abs price-bar" style="top:436px"><span>120G</span><span>$6.00</span><span>$11.00</span></div>
    <p class="abs item-name" style="top:451px">Mountain Pepper and Dark Berry</p>
    <div class="abs price-bar" style="top:466px"><span>120G</span><span>$6.00</span><span>$11.00</span></div>
    <p class="abs item-name" style="top:480px">Highland Fern</p>
    <div class="abs price-bar" style="top:495px"><span>120G</span><span>$6.00</span><span>$11.00</span></div>
  </article>

  <!-- Order form -->
  <article class="panel panel--c order">
    <div class="photo order__photo" role="img" aria-label="Photo of a woman in a towel holding a lit candle jar"></div>
    <svg class="bg-svg" width="215" height="514" viewBox="0 0 215 514" aria-hidden="true">
      <path d="M0 196 C50 170 120 160 215 140 L215 484 C150 470 70 470 0 478 Z" fill="#3b4038"/>
      <path d="M0 188 C50 162 120 150 215 128 L215 136 C120 156 50 166 0 194 Z" fill="#f1e8d8"/>
    </svg>
    <div class="abs badge"><span>25%</span><span>OFF</span></div>
    <h2 class="abs display order__title">Larkfield<br>Seedhouse CO.</h2>
    <div class="abs order__copy">
      <p>Please see our wholesale list for 2025 below.If you don't have a preferred purchase order format, please use this sheet when placing orders. Please send email orders to orders@larkfieldseedhouse.co</p>
      <p>For bulk supplies or any products for our website not covered below please contact us directly to discuss.</p>
      <p>Freight to anywhere in Australia is an additional cost.</p>
      <p>Please contact Nora or Glen on 0412 555 018 or reach out to us at hello@larkfieldseedhouse.co if you have any questions.</p>
    </div>
    <div class="abs form">
      <div class="form__row"><span>Business Name:</span><i></i></div>
      <div class="form__row"><span>Primary Contact:</span><i></i></div>
      <div class="form__row"><span>Email:</span><i></i></div>
      <div class="form__row"><span>Phone:</span><i></i></div>
      <div class="form__row"><span>Postal Address:</span><i></i></div>
      <div class="form__row"><span>ABN (initial orders only):</span><i></i></div>
      <div class="form__row"><span>Email for Accounts:</span><i></i></div>
    </div>
    <p class="abs order__web"><span class="globe"></span>www.larkfieldseedhouseco.com.au</p>
  </article>
</section>

<!-- ============ INSIDE SPREAD ============ -->
<section class="spread spread--inside">

  <!-- Ingredients -->
  <article class="panel panel--a inside-a">
    <div class="photo strip-photo" style="width:220px" role="img" aria-label="Photo of amber candle jars and bottles among succulents"></div>
    <svg class="bg-svg" width="220" height="110" viewBox="0 0 220 110" aria-hidden="true">
      <path d="M0 110 V88 C40 70 100 72 150 60 C180 52 205 40 220 30 V110 Z" fill="#f3ebdd"/>
      <path d="M0 88 C40 70 100 72 150 60 C180 52 205 40 220 30 V38 C205 48 180 60 150 67 C100 78 40 78 0 96 Z" fill="#3b4038"/>
    </svg>

    <div class="photo feature-img" style="left:13px;top:103px" role="img" aria-label="Photo of a red soy wax candle jar"></div>
    <div class="abs" style="left:97px;top:106px;width:112px">
      <h3 class="feature-title">Soy Wax</h3><div class="feature-rule"></div>
      <p class="feature-text">Soy wax is a natural vegetable wax derived from soybeans. It burns cleanly with minimal soot and offers an excellent hot and cold scent throw.</p>
    </div>

    <div class="photo feature-img feature-img--r" style="left:125px;top:181px" role="img" aria-label="Photo of a white coconut wax candle on wood"></div>
    <div class="abs feature--r" style="left:12px;top:184px;width:106px">
      <h3 class="feature-title">Coconut Wax</h3><div class="feature-rule" style="margin-left:6px"></div>
      <p class="feature-text">oburns cooler and longer than many other waxes. Vegan-friendly and eco-conscious, it provides a soft, smooth finish to our candle blends.</p>
    </div>

    <div class="photo feature-img" style="left:13px;top:259px;background:linear-gradient(135deg,#efe9df,#a9a094)" role="img" aria-label="Photo of white candle tins"></div>
    <div class="abs" style="left:97px;top:262px;width:114px">
      <h3 class="feature-title">Tasmanian Leatherwood</h3><div class="feature-rule"></div>
      <p class="feature-text">Wild-sourced from Tasmania, this premium beeswax adds natural structure and hardness to our candles. It burns brightly and cleanly while releasing a gentle, honey-like aroma.</p>
    </div>

    <div class="photo feature-img feature-img--r" style="left:125px;top:341px;background:linear-gradient(135deg,#e8e2cf,#9fa07e)" role="img" aria-label="Photo of stacked handmade soap bars"></div>
    <div class="abs feature--r" style="left:12px;top:344px;width:106px">
      <h3 class="feature-title">Wooden Wicks</h3><div class="feature-rule" style="margin-left:6px"></div>
      <p class="feature-text">lead-free, zinc-free natural cotton wicks or sustainably sourced wooden wicks. Cotton wicks provide a stable, classic burn, while wooden wicks offer an atmospheric soft crackle.</p>
    </div>

    <div class="photo feature-img" style="left:13px;top:427px;background:linear-gradient(135deg,#7d6a55,#2f2a25)" role="img" aria-label="Photo of a hand holding an amber spray bottle"></div>
    <div class="abs" style="left:97px;top:430px;width:114px">
      <h3 class="feature-title">Premium Fragrance Oils</h3><div class="feature-rule"></div>
      <p class="feature-text">We use phthalate-free fragrance oils and pure essential oils to create our signature scent profiles. Many scents are inspired by or derived from Tasmanian botanicals including Blue.</p>
    </div>
  </article>

  <!-- Oils and actives -->
  <article class="panel panel--b inside-b">
    <div class="photo strip-photo" style="width:230px" role="img" aria-label="Photo of candle jars and antlers on a wooden table"></div>
    <svg class="bg-svg" width="230" height="100" viewBox="0 0 230 100" aria-hidden="true">
      <path d="M0 72 C60 68 130 70 230 58 V100 H0 Z" fill="#3b4038"/>
      <path d="M150 72 C190 66 215 62 230 56 V62 C212 68 190 72 160 76 Z" fill="#f1e8d8"/>
    </svg>

    <div class="abs" style="left:15px;top:108px;width:90px">
      <h3 class="oil-title">Shea Butter</h3>
      <p class="oil-text">Shea butter is extracted from the nut of the shea tree and is rich in fatty acids and vitamins. It softens and.</p>
    </div>
    <div class="thumb" style="left:115px;top:105px;width:48px;height:42px" role="img" aria-label="Photo of a candle jar in sunlight"></div>
    <div class="thumb" style="left:168px;top:105px;width:48px;height:42px" role="img" aria-label="Photo of a small oil bottle"></div>
    <div class="abs" style="left:15px;top:155px;width:90px;height:.6px;background:#8e9088"></div>

    <div class="abs" style="left:15px;top:163px;width:92px">
      <h3 class="oil-title">Tasmanian Olive Oil</h3>
      <p class="oil-text">Shea butter is extracted from the nut of the shea tree and is rich in fatty acids and vitamins. It softens and.</p>
    </div>
    <div class="thumb" style="left:115px;top:154px;width:48px;height:41px" role="img" aria-label="Photo of glass perfume bottles"></div>
    <div class="thumb" style="left:168px;top:154px;width:48px;height:41px;background:linear-gradient(135deg,#f0ede8,#6c5a48)" role="img" aria-label="Photo of candle jars on white"></div>

    <div class="thumb" style="left:15px;top:218px;width:83px;height:69px;border-radius:30px 6px 30px 6px;background:linear-gradient(135deg,#9b7d5c,#3a2d22)" role="img" aria-label="Photo of an amber bottle with antlers"></div>
    <div class="abs" style="left:114px;top:216px;width:110px">
      <h3 class="oil-title">Sodium Hydroxide</h3>
      <p class="oil-text">Sodium hydroxide (lye) is essential for the saponification process and is not present in the finished product.</p>
      <ul class="ticks" style="margin-top:6px">
        <li><span class="tick">✓</span>Purification</li><li><span class="tick">✓</span>Cleansing</li>
        <li><span class="tick">✓</span>Saponifying</li><li><span class="tick">✓</span>Purifying</li>
        <li><span class="tick">✓</span>Neutralizing</li><li><span class="tick">✓</span>Processing</li>
      </ul>
    </div>

    <div class="abs" style="left:15px;top:299px;width:95px">
      <h3 class="oil-title">Lavender Meadow</h3>
      <p class="oil-text">A soothing, herbaceous floral fragrance that evokes the calm of Tasmanian lavender fields.</p>
      <ul class="ticks" style="margin-top:6px">
        <li><span class="tick">✓</span>Calming</li><li><span class="tick">✓</span>Soothing</li>
        <li><span class="tick">✓</span>Comforting</li><li><span class="tick">✓</span>Refreshing</li>
      </ul>
    </div>
    <div class="thumb" style="left:115px;top:303px;width:48px;height:40px;background:linear-gradient(135deg,#e8e2cf,#8c8a6a)" role="img" aria-label="Photo of a reed diffuser"></div>
    <div class="thumb" style="left:168px;top:303px;width:48px;height:40px;background:linear-gradient(135deg,#f5f3ef,#7a6a5a)" role="img" aria-label="Photo of pump bottles and jars"></div>

    <div class="thumb" style="left:15px;top:375px;width:49px;height:42px" role="img" aria-label="Photo of amber bottles"></div>
    <div class="thumb" style="left:70px;top:375px;width:49px;height:42px;background:linear-gradient(135deg,#e9ecef,#35627a)" role="img" aria-label="Photo of a blue balm tin"></div>
    <div class="thumb" style="left:15px;top:421px;width:49px;height:42px" role="img" aria-label="Photo of candles on a shelf"></div>
    <div class="thumb" style="left:70px;top:421px;width:49px;height:42px;background:linear-gradient(135deg,#c45b37,#2b2520)" role="img" aria-label="Photo of candle jars in warm light"></div>

    <div class="abs" style="left:131px;top:374px;width:93px">
      <h3 class="oil-title">Tasmanian Leatherwood</h3>
      <p class="oil-text">An outstanding natural emollient that hydrates, protects, softens and soothes the skin.</p>
    </div>
    <div class="abs" style="left:131px;top:427px;width:93px">
      <h3 class="oil-title">Coconut Oil</h3>
      <p class="oil-text">Coconut oil is easily absorbed and rich in vitamins E and K. Its antifungal, antibacterial.</p>
    </div>

    <div class="abs contact"></div>
    <svg class="bg-svg" style="top:460px" width="230" height="30" viewBox="0 0 230 30" aria-hidden="true">
      <path d="M0 24 C80 18 160 10 230 4 V18 C160 22 80 26 0 30 Z" fill="#3b4038"/>
      <path d="M120 18 C170 12 205 8 230 2 V8 C205 14 170 18 130 22 Z" fill="#d9b23c"/>
    </svg>
    <div class="abs" style="left:0;top:476px;width:230px;height:38px">
      <p class="abs contact__head">CONTACT INFO:</p>
      <p class="abs contact__line"><span>☎ 0412 555 018</span><span>✉ hello@larkfieldseedhouse.co</span><span><span class="globe" style="width:5px;height:5px"></span>larkfieldseedhouseco.com.au</span></p>
    </div>
  </article>

  <!-- Scents -->
  <article class="panel panel--c inside-c">
    <div class="abs scent-head"></div>
    <svg class="bg-svg" width="215" height="140" viewBox="0 0 215 140" aria-hidden="true">
      <path d="M0 96 H100 V0 H215 V30 C200 40 190 70 195 100 H100 Z" fill="#3b4038"/>
    </svg>
    <div class="abs brand-mark scent-logo">LSCo.</div>
    <p class="abs scent-tagline">Thoughtfully crafted in small batches, our botanical range reflects the calm,</p>
    <h2 class="abs display scent-heading">Handcrafted<br>Botanical<br>Products</h2>
    <div class="photo arch" style="left:100px;top:37px;width:36px;height:100px" role="img" aria-label="Photo of a woman with a hair towel"></div>
    <div class="photo arch" style="left:141px;top:37px;width:57px;height:100px" role="img" aria-label="Photo of a woman applying face cream"></div>

    <div class="abs" style="left:14px;top:102px;width:82px">
      <h3 class="display" style="font-size:10px;color:#3b4038">Main Scents</h3>
      <p class="col-text" style="font-size:4.4px">Our signature scents are inspired by the Tasmanian landscape—calming, refreshing, and beautifully balanced. Each fragrance is crafted to create a gentle, lasting sensory experience.</p>
    </div>

    <div class="abs" style="left:14px;top:153px;width:102px">
      <h3 class="col-title">Wild Highland Fern</h3><div class="col-rule"></div>
      <p class="col-text">Our most popular scent. A blend of fresh bergamot top notes and creamy vanilla bean, softened by a delicate whisper of magnolia. This scent conjures the vast.</p>
    </div>
    <div class="thumb" style="left:14px;top:196px;width:47px;height:40px;background:linear-gradient(135deg,#6d7a86,#2b2f33)" role="img" aria-label="Photo of a dark candle jar"></div>
    <div class="thumb" style="left:68px;top:196px;width:47px;height:40px;background:linear-gradient(135deg,#e4dbe9,#8a6fa0)" role="img" aria-label="Photo of a lavender candle jar"></div>
    <div class="thumb" style="left:14px;top:244px;width:47px;height:40px;background:linear-gradient(135deg,#eee7da,#b79f7c)" role="img" aria-label="Photo of cream candle jars"></div>
    <div class="thumb" style="left:68px;top:244px;width:47px;height:40px" role="img" aria-label="Photo of a gift pack with a bottle"></div>

    <div class="abs" style="left:14px;top:297px;width:102px">
      <h3 class="col-title">Windswept Southern Shoreline</h3><div class="col-rule"></div>
      <p class="col-text">Bold and textured with aromatic cypress pine, enriched by warm sandalwood and patchouli, and finished with a soft hint of jasmine.</p>
    </div>
    <div class="abs" style="left:14px;top:343px;width:102px">
      <h3 class="col-title">Old Cedar Grove</h3><div class="col-rule"></div>
      <p class="col-text">A crisp, forest-infused fragrance featuring cypress and Tasmanian blue gum with spirited lemon zest. Mid-notes of fir balsam and fresh pine needles lead into a base of cedarwood, patchouli and white musk. Evokes the ancient Tasmanian forests in full bloom.</p>
    </div>
    <div class="photo arch" style="left:13px;top:403px;width:33px;height:90px;border-radius:16px 16px 4px 4px;background:linear-gradient(180deg,#aab19b,#5d6552)" role="img" aria-label="Photo of eucalyptus leaves and soap"></div>
    <div class="photo arch" style="left:50px;top:403px;width:50px;height:90px;border-radius:24px 24px 4px 4px;background:linear-gradient(180deg,#9a7b58,#2e2720)" role="img" aria-label="Photo of a lit candle with dried flowers"></div>

    <div class="abs" style="left:134px;top:150px;width:75px">
      <h3 class="display why">Why<small>Choose Us</small></h3>
      <p class="col-text" style="margin-top:6px">Choose us for thoughtfully crafted small-batch botanical products made with pure ingredients and honest methods. We prioritise quality, sustainability, and a beautiful customer experience.</p>
      <h3 class="col-title" style="margin-top:9px">Lavender Meadow</h3><div class="col-rule"></div>
      <p class="col-text">A soothing, herbaceous floral fragrance that evokes the calm of Tasmanian lavender fields. Clean and intrinsically relaxing, Lavender Meadow is perfect for moments of rest or reflection.</p>
    </div>
    <div class="thumb" style="left:135px;top:296px;width:65px;height:56px;border-radius:4px 18px 4px 18px;background:linear-gradient(135deg,#d8c3a2,#3d4a5a)" role="img" aria-label="Photo of a candle jar among soap bars"></div>
    <div class="abs" style="left:134px;top:361px;width:75px">
      <h3 class="col-title">Alpine Dew</h3><div class="col-rule"></div>
      <p class="col-text">A bright, fresh scent of Granny Smith apple and pomegranate uplifted with a minty edge and rounded off by a base of soft vanilla.</p>
      <h3 class="col-title" style="margin-top:8px">Dark Berry</h3><div class="col-rule"></div>
      <p class="col-text">A luscious and vibrant blend of blackberry and raspberry, touched with subtle jasmine and vanilla sweetness, and warmed by a hint of native Tasmanian pepperberry.</p>
      <ul class="mini-ticks" style="margin-top:6px">
        <li><span class="tick">✓</span>Purification</li><li><span class="tick">✓</span>Purification</li>
        <li><span class="tick">✓</span>Purification</li><li><span class="tick">✓</span>Purification</li>
        <li><span class="tick">✓</span>Purification</li><li><span class="tick">✓</span>Purification</li>
      </ul>
    </div>
  </article>
</section>

</body>
</html>
```